YARD FRONTS "N" MORE

catyering to driveway/patio floor construction and remodeling. Concrete, concrete pavers, asphalt, Landscaping, irrigation, pergolas and pools.

Target Market(s)

the home owner that wants to enhance their home

Industry/Entity Type

construction

Contact Information for Business Card

presidet: tomas bellweather email: yardfrontsnmore@example.come office/cell: 555 214 8830

Font styles to use
Sans Serif

Requirements
Must have
• logo should pop out
Nice to have
• the logo should demonstrate that we do exteriors only

```html
<!DOCTYPE html>
<html lang="en">
<head>
<meta charset="utf-8">
<title>Tomas Bellweather – Business Card</title>
<link href="https://fonts.googleapis.com/css2?family=Open+Sans:wght@400;600;700;800&display=swap" rel="stylesheet">
<style>
  :root {
    --bg: #262626;
    --card: #1f1f22;
    --card-back: #1a1a1c;
    --red: #e3161f;
    --white: #f2f2f2;
    --grey: #9a9a9c;
    --emboss: #3b3b3f;
  }
  * { margin: 0; padding: 0; box-sizing: border-box; }
  html, body {
    width: 1200px; height: 780px; overflow: hidden;
    background: var(--bg);
    font-family: "Open Sans", Arial, sans-serif;
  }
  .canvas {
    position: relative; width: 1200px; height: 780px;
    display: flex; align-items: center; justify-content: center; gap: 40px;
  }
  .card {
    position: relative; width: 560px; height: 320px;
    background: var(--card); overflow: hidden;
    box-shadow: 0 10px 30px rgba(0,0,0,.45);
  }
  .card--back { background: var(--card-back); }

  /* front: logo block rotated along the left edge */
  .brand-side {
    position: absolute; left: 0; top: 0; width: 120px; height: 320px;
    display: flex; align-items: center; justify-content: center;
  }
  .brand-mark {
    transform: rotate(-90deg);
    display: flex; align-items: center; gap: 10px; white-space: nowrap;
  }
  .brand-mark__name {
    font-weight: 700; font-size: 30px; color: var(--grey); letter-spacing: .5px;
  }
  .brand-mark__square { width: 14px; height: 14px; background: var(--red); }

  .accent-bar {
    position: absolute; right: 0; top: 22px; width: 12px; height: 64px;
    background: var(--red);
  }

  .contact {
    position: absolute; right: 30px; top: 20px;
    text-align: right; color: var(--white);
  }
  .contact__name { font-size: 25px; font-weight: 700; line-height: 1.15; color: var(--grey); }
  .contact__name .first { color: var(--red); }
  .contact__title { font-size: 14px; font-weight: 700; margin-bottom: 5px; }
  .contact__line {
    font-size: 12.5px; line-height: 1.45;
    display: flex; justify-content: flex-end; align-items: center; gap: 6px;
  }
  .contact__line svg { width: 11px; height: 11px; fill: var(--red); }

  .services { margin-top: 6px; }
  .services__title { font-size: 15px; font-weight: 700; color: var(--red); line-height: 1.3; }
  .services__list { list-style: none; }
  .services__item {
    font-size: 13px; line-height: 1.32;
    display: flex; justify-content: flex-end; align-items: center; gap: 8px;
  }
  .services__item::after {
    content: ""; width: 8px; height: 8px; border-radius: 50%; background: var(--red);
  }

  /* back: embossed logo */
  .back-mark {
    position: absolute; inset: 0;
    display: flex; align-items: center; justify-content: center; gap: 14px;
  }
  .back-mark__name {
    font-weight: 800; font-size: 44px; color: var(--emboss);
  }
  .back-mark__square { width: 20px; height: 20px; background: var(--emboss); }
</style>
</head>
<body>
<main class="canvas">

  <section class="card card--front" aria-label="Business card front">
    <div class="brand-side">
      <div class="brand-mark">
        <span class="brand-mark__name">Tomas Bellweather</span>
        <span class="brand-mark__square"></span>
      </div>
    </div>

    <div class="accent-bar"></div>

    <div class="contact">
      <h1 class="contact__name"><span class="first">Tomas</span> Bellweather</h1>
      <p class="contact__title">Presidet</p>
      <p class="contact__line">555 214 8830
        <svg viewBox="0 0 24 24" aria-hidden="true"><path d="M6.6 10.8a15.1 15.1 0 0 0 6.6 6.6l2.2-2.2a1 1 0 0 1 1-.25 11.4 11.4 0 0 0 3.6.57 1 1 0 0 1 1 1V20a1 1 0 0 1-1 1A17 17 0 0 1 3 4a1 1 0 0 1 1-1h3.5a1 1 0 0 1 1 1c0 1.25.2 2.45.57 3.57a1 1 0 0 1-.25 1z"/></svg>
      </p>
      <p class="contact__line">yardfrontsnmore@example.come
        <svg viewBox="0 0 24 24" aria-hidden="true"><path d="M2 5h20v14H2zm2 2v.5l8 5 8-5V7l-8 5z"/></svg>
      </p>

      <div class="services">
        <h2 class="services__title">SERVICES</h2>
        <ul class="services__list">
          <li class="services__item">Concrete</li>
          <li class="services__item">Asphalt</li>
          <li class="services__item">Irrigation</li>
          <li class="services__item">Landscaping</li>
          <li class="services__item">Concrete pavers</li>
          <li class="services__item">Pergolas and pools</li>
          <li class="services__item">Catyering to driveway</li>
          <li class="services__item">Patio floor construction and remodeling</li>
        </ul>
      </div>
    </div>
  </section>

  <section class="card card--back" aria-label="Business card back">
    <div class="back-mark">
      <span class="back-mark__name">Tomas Bellweather</span>
      <span class="back-mark__square"></span>
    </div>
  </section>

</main>
</body>
</html>
```